Quillmark Select

Letter Head, Envelope, Business Cards, Social Media Banner (FB/Twitter), Social Media Icon, Social Media Announcement Template...

We are a Softball Team/Organization

Target Market(s)

High School Student-Athletes (softball players) and their parents

Font styles to use
Serif

Requirements
Must have
• Logo & Colors
Must POP and say WOW
Common theme amongst all designs

```html
<!DOCTYPE html>
<html lang="en">
<head>
<meta charset="utf-8">
<title>Quillmark Select Stationery</title>
<link rel="stylesheet" href="https://fonts.googleapis.com/css2?family=Tinos:wght@400;700&family=Lato:wght@300;400;700&family=Great+Vibes&display=swap">
<style>
  :root {
    --navy: #1e3363;
    --navy-deep: #1a2c57;
    --navy-light: #2c4a8a;
    --paper: #f3f3f3;
    --paper-edge: #e9e9e9;
    --stage: #e4e4e4;
    --ink: #111;
    --body-ink: #555;
    --band-grey: #c9c9c9;
  }
  * { margin: 0; padding: 0; box-sizing: border-box; }
  html, body { width: 1200px; height: 942px; overflow: hidden; }
  body {
    background: var(--stage);
    position: relative;
    font-family: "Tinos", "Times New Roman", serif;
    color: var(--ink);
  }
  .sheet {
    position: absolute;
    background: var(--paper);
    box-shadow: 0 2px 6px rgba(0,0,0,.12);
    overflow: hidden;
  }

  /* wordmark */
  .wordmark {
    position: absolute;
    font-family: "Tinos", "Times New Roman", serif;
    font-weight: 700;
    color: var(--navy);
    line-height: 1;
    text-transform: uppercase;
  }
  .wordmark span { display: block; }
  .wordmark .wm-top { letter-spacing: .06em; }
  .wordmark .wm-bottom { letter-spacing: .32em; margin-top: 2px; }
  .wordmark.on-dark { color: #fff; }

  /* band */
  .footer-band {
    position: absolute; left: 0; right: 0;
    display: flex;
  }
  .footer-band .band-main {
    background: var(--navy);
    color: #fff;
    display: flex; align-items: center;
  }
  .footer-band .band-fade {
    flex: 1;
    background: linear-gradient(90deg, #9a9a9a, var(--paper));
  }

  .social-row { display: flex; align-items: center; }
  .social-row .dot {
    display: inline-block; border-radius: 50%;
    background: var(--navy);
  }

  /* letterhead */
  .letterhead { left: 157px; top: 151px; width: 436px; height: 617px; }
  .letterhead .wordmark { left: 32px; top: 26px; }
  .letterhead .wm-top { font-size: 22px; }
  .letterhead .wm-bottom { font-size: 9.5px; }
  .letterhead-contact {
    position: absolute; left: 292px; top: 26px;
    font-size: 7px; line-height: 9px;
  }
  .letterhead-contact .gap { margin-top: 3px; }
  .icon-line { display: flex; align-items: center; gap: 4px; }
  .icon-line svg { width: 6px; height: 6px; fill: var(--navy); }
  .letter {
    position: absolute; left: 63px; top: 134px; width: 310px;
    font-family: "Lato", Arial, sans-serif; font-weight: 300;
    font-size: 7px; line-height: 10.2px; color: var(--body-ink);
  }
  .letter .recipient-name { font-weight: 700; color: #222; }
  .letter p { margin-bottom: 10.2px; text-align: justify; }
  .letter .date { margin-bottom: 10px; }
  .letter .recipient { margin-bottom: 16px; }
  .letter .salutation { margin-bottom: 10px; }
  .letter .closing { margin-top: 30px; margin-bottom: 0; }
  .letter .signature {
    font-family: "Great Vibes", cursive;
    font-size: 15px; color: #222; margin-top: 4px;
  }
  .letterhead .social-row {
    position: absolute; top: 585px; left: 0; right: 0;
    justify-content: center; gap: 7px; font-size: 7px;
  }
  .letterhead .social-row .dot { width: 6px; height: 6px; margin-right: 3px; }
  .letterhead .footer-band { top: 599px; height: 11px; }
  .letterhead .band-main { width: 386px; justify-content: center; font-size: 7px; padding-left: 0; }

  /* business card front */
  .card-front { left: 625px; top: 139px; width: 227px; height: 130px; }
  .card-front .wordmark { left: 20px; top: 56px; }
  .card-front .wm-top { font-size: 13.5px; }
  .card-front .wm-bottom { font-size: 5.8px; margin-top: 1px; }
  .card-front .divider {
    position: absolute; left: 114px; top: 40px; width: 1px; height: 49px;
    background: #888;
  }
  .card-details {
    position: absolute; left: 124px; top: 40px;
    font-size: 4.6px; line-height: 6px;
  }
  .card-details .person { font-size: 6.6px; font-weight: 700; color: var(--navy); line-height: 7px; }
  .card-details .gap { margin-top: 5px; }
  .card-details .icon-line svg { width: 4px; height: 4px; }
  .card-details .icon-line { gap: 3px; }
  .card-front .social-row {
    position: absolute; top: 104px; left: 0; right: 0;
    justify-content: center; gap: 4px; font-size: 4.6px;
  }
  .card-front .social-row .dot { width: 4px; height: 4px; margin-right: 2px; }
  .card-front .footer-band { top: 115px; height: 8px; }
  .card-front .band-main { width: 200px; justify-content: center; font-size: 4.6px; }

  /* business card back */
  .card-back {
    left: 897px; top: 139px; width: 227px; height: 130px;
    background: linear-gradient(120deg, var(--navy-deep) 45%, var(--navy-light));
  }
  .card-back .wordmark { left: 22px; top: 50px; }
  .card-back .wm-top { font-size: 14.5px; }
  .card-back .wm-bottom { font-size: 6.2px; margin-top: 1px; }

  /* envelope front */
  .envelope-front { left: 624px; top: 297px; width: 501px; height: 217px; }
  .envelope-front .wordmark { left: 30px; top: 36px; }
  .envelope-front .wm-top { font-size: 22px; }
  .envelope-front .wm-bottom { font-size: 9.5px; }
  .envelope-contact {
    position: absolute; left: 29px; top: 132px;
    font-size: 7px; line-height: 8.9px;
  }
  .envelope-contact .gap { margin-top: 4px; }
  .envelope-contact .dot {
    display: inline-block; width: 6px; height: 6px; border-radius: 50%;
    background: var(--navy);
  }
  .envelope-contact .icon-line svg { width: 6px; height: 6px; }
  .envelope-front .footer-band { top: 197px; height: 10px; }
  .envelope-front .band-main { width: 445px; font-size: 7px; padding-left: 29px; }

  /* envelope back */
  .envelope-back { left: 624px; top: 550px; width: 501px; height: 217px; background: transparent; box-shadow: none; }
  .envelope-back svg.envelope-shape { position: absolute; inset: 0; }
  .envelope-back .wordmark { left: 0; right: 0; top: 24px; text-align: center; }
  .envelope-back .wm-top { font-size: 14.5px; }
  .envelope-back .wm-bottom { font-size: 6.2px; margin-top: 1px; }
</style>
</head>
<body>

<!-- Letterhead -->
<section class="sheet letterhead">
  <div class="wordmark"><span class="wm-top">Quillmark</span><span class="wm-bottom">Select</span></div>

  <address class="letterhead-contact" style="font-style:normal">
    <div>Quillmark Select</div>
    <div>Larkfield, Ohio 40512, US</div>
    <div class="icon-line gap"><svg viewBox="0 0 10 10"><path d="M2 1l2 0 1 2.5-1.2 1a5 5 0 0 0 2.7 2.7l1-1.2L10 7v2a1 1 0 0 1-1 1A8 8 0 0 1 1 2a1 1 0 0 1 1-1z"/></svg>555-014-2290</div>
    <div class="icon-line"><svg viewBox="0 0 10 10"><path d="M0 2h10v6H0z M0 2l5 3.5L10 2" fill="none" stroke="#1e3363" stroke-width="1.2"/></svg>pitchandplate.team@mailbox.net</div>
  </address>

  <div class="letter">
    <div class="date">01 January 2050</div>
    <div class="recipient">
      <div class="recipient-name">Company (Pvt) Ltd.</div>
      <div>PO Box 3355 Mainville St</div>
      <div>Sample City Country 3355</div>
    </div>
    <div class="salutation">Dear Owen Radley,</div>
    <p>Lorem ipsum dolor sit amet, consectetuer adipiscing elit, sed diam nonummy nibh euismod tincidunt ut laoreet dolore magna aliquam erat volutpat. Ut wisi enim ad minim veniam, quis nostrud exerci tation ullamcorper suscipit lobortis nisl ut aliquip ex ea commodo consequat. Duis dolore te feugait nulla facilisi. Nam liber tempor cum soluta nobis eleifend option congue nihil imperdiet doming id quod mazim placerat facer possim assum. Lorem ipsum dolor sit amet, consectetuer adipiscing elit, sed diam nonummy nibh euismod tincidunt ut laoreet dolore magna aliquam erat volutpat. Ut wisi enim ad minim veniam, quis nostrud exerci tation ullamcorper suscipit lobortis nisl ut aliquip ex ea commodo consequat.</p>
    <p>Consectetuer adipiscing elit, sed diam nonummy nibh euismod tincidunt ut laoreet dolore magna aliquam erat volutpat. Ut wisi enim ad minim veniam, quis nostrud exerci tation ullamcorper suscipit lobortis nisl ut aliquip ex ea commodo consequat. Consectetuer adipiscing elit, sed diam nonummy nibh euismod tincidunt ut laoreet dolore magna aliquam erat volutpat. Ut wisi enim ad minim veniam, quis nostrud exerci tation ullamcorper suscipit lobortis nisl ut aliquip ex ea commodo consequat.</p>
    <p>Consectetuer adipiscing elit, sed diam nonummy nibh euismod tincidunt ut laoreet dolore magna aliquam erat volutpat. Ut wisi enim ad minim veniam, quis nostrud exerci tation ullamcorper suscipit lobortis nisl ut aliquip ex ea commodo consequat. Consectetuer adipiscing elit, sed diam nonummy nibh euismod tincidunt ut laoreet dolore magna aliquam erat volutpat. Ut wisi enim ad minim veniam, quis nostrud exerci tation ullamcorper suscipit lobortis nisl ut aliquip ex ea commodo consequat.</p>
    <p class="closing">Sincerely Yours</p>
    <div class="signature">Marcus Ellery Vance</div>
  </div>

  <div class="social-row">
    <span><i class="dot"></i>/QuillmarkSelect</span>
    <span><i class="dot"></i>/Quillmark.Select.Team</span>
    <span><i class="dot"></i>@QuillmarkSelect</span>
  </div>
  <div class="footer-band"><div class="band-main">QuillmarkSelect.com</div><div class="band-fade"></div></div>
</section>

<!-- Business card front -->
<section class="sheet card-front">
  <div class="wordmark"><span class="wm-top">Quillmark</span><span class="wm-bottom">Select</span></div>
  <div class="divider"></div>
  <div class="card-details">
    <div class="person">Dana Whitcombe</div>
    <div>Founder &amp; CEO</div>
    <div class="gap">Quillmark Select</div>
    <div>Larkfield, Ohio 40512, US</div>
    <div class="icon-line gap"><svg viewBox="0 0 10 10"><path d="M2 1l2 0 1 2.5-1.2 1a5 5 0 0 0 2.7 2.7l1-1.2L10 7v2a1 1 0 0 1-1 1A8 8 0 0 1 1 2a1 1 0 0 1 1-1z"/></svg>555-014-2290</div>
    <div class="icon-line"><svg viewBox="0 0 10 10"><path d="M0 2h10v6H0z M0 2l5 3.5L10 2" fill="none" stroke="#1e3363" stroke-width="1.2"/></svg>pitchandplate.team@mailbox.net</div>
  </div>
  <div class="social-row">
    <span><i class="dot"></i>/QuillmarkSelect</span>
    <span><i class="dot"></i>/Quillmark.Select.Team</span>
    <span><i class="dot"></i>@QuillmarkSelect</span>
  </div>
  <div class="footer-band"><div class="band-main">QuillmarkSelect.com</div><div class="band-fade"></div></div>
</section>

<!-- Business card back -->
<section class="sheet card-back">
  <div class="wordmark on-dark"><span class="wm-top">Quillmark</span><span class="wm-bottom">Select</span></div>
</section>

<!-- Envelope front -->
<section class="sheet envelope-front">
  <div class="wordmark"><span class="wm-top">Quillmark</span><span class="wm-bottom">Select</span></div>
  <address class="envelope-contact" style="font-style:normal">
    <div>Quillmark Select</div>
    <div>Larkfield, Ohio 40512, US</div>
    <div class="icon-line gap"><i class="dot"></i>/QuillmarkSelect</div>
    <div class="icon-line"><i class="dot"></i>/Quillmark.Select.Team</div>
    <div class="icon-line"><i class="dot"></i>@QuillmarkSelect</div>
    <div class="icon-line"><svg viewBox="0 0 10 10"><path d="M0 2h10v6H0z M0 2l5 3.5L10 2" fill="none" stroke="#1e3363" stroke-width="1.2"/></svg>pitchandplate.team@mailbox.net</div>
  </address>
  <div class="footer-band"><div class="band-main">QuillmarkSelect.com</div><div class="band-fade"></div></div>
</section>

<!-- Envelope back -->
<section class="sheet envelope-back">
  <svg class="envelope-shape" width="501" height="217" viewBox="0 0 501 217">
    <rect x="0" y="0" width="501" height="217" fill="#f3f3f3"/>
    <path d="M14 60 L14 205 Q14 214 6 216 M487 60 L487 205 Q487 214 495 216" fill="none" stroke="#d2d2d2" stroke-width="0.8"/>
    <path d="M0 0 H501 L488 56 Q485 71 470 71 H31 Q16 71 13 56 Z" fill="var(--navy)"/>
  </svg>
  <div class="wordmark on-dark"><span class="wm-top">Quillmark</span><span class="wm-bottom">Select</span></div>
</section>

</body>
</html>
```